Brolvix Services Brochure

We need a brochure designed for each of the various services we offer to residents of the state of Tasmania, Australia. We provide internet and communications solutions for both residential/home office and businesses, as well as rural communications solutions for the Huon Valley region. These brochures will detail our offerings and the types and prices of plans available.
BROCHURE TEXT
Cover page: Big heading:
Brolvix
Clever, cost effective data communications
Internet Plans for Businesses
Picture?
Inside page 1: Brolvix clever, cost effective data communications
Brolvix internet and data business solutions provide customers with connectivity and networking options with proven speed and reliability across multiple locations and hundreds of users, including hard-to-reach areas. The unique Brolvix infrastructure network allows us to do this without compromising quality, speed and reliability.
Middle inside page: Business-Grade Internet
Connecting some of Tasmania’s most rural areas with fast and reliable business-grade internet is what we do best. Brolvix offers options to connect and interconnect your business, no matter where your offices are located. Our team will work with you to determine the best plans, connections and options to suit your business.
Brolvix’s Business Internet Solutions
Corporate Internet
Highly reliable internet that is perfect for everyday company operations such as video conferencing, sending and receiving large files and setting up online storage facilities.
Small Business Internet
For smaller organisations needing business-grade internet but not quite at the corporate level.
Not sure?
Call us – we will explain our services in a language you understand.
Inside third page Pricing
Clever, cost effective plans
Basic plans starting from $49.00
The Brolvix team is dedicated to working with you to determine the best solution for your business communication needs. Our plans are flexible and we don’t believe you should feel stuck with your plan when your situation changes, we will help you adapt your package whenever you need us to. Easy as that!
Pricing Options
Corporate Internet $150.00
Brolvix has a wide range of corporate options to suit businesses of all sizes. Our most basic corporate plans start from $150 for 512/512k 50GB.
Small Business Internet $49.00
Brolvix small business internet solutions are perfect for smaller organisations who require a business grade connection on a smaller scale. Our most basic small business plans start from $49.00 for 512/512k 10GB.
Back page:
Ask us about additional business services such as managed network services, server hosting, wireless point-to-point links, Zephon wireless LAN, co-Location and CCTV services to see how we can provide a full business communications package for you.
These solutions are detailed in our Business Services brochure or can be found on our website.
Contact Us
www.brolvix.com.au
Phone - 1300 418 265
Fax - 1300 418 947
Email - sales@brolvix.com.au
Brolvix – clever, cost effective data communications
Please see attached style guide
Target Market(s)
Small and medium businesses in Tasmania, Australia.
Industry/Entity Type
Communications
Look and feel

```html
<!DOCTYPE html>
<html lang="en">
<head>
<meta charset="utf-8">
<title>Brolvix – Business Internet Brochure</title>
<link rel="stylesheet" href="https://fonts.googleapis.com/css2?family=Carlito:wght@400;700&family=Cinzel:wght@700&display=swap">
<style>
  :root {
    --frame-grey: #bdbdbd;
    --blue-deep: #3b72b6;
    --blue-mid: #5a8ccb;
    --blue-light: #8fb5e0;
    --orange: #ec7428;
    --white: #ffffff;
    --sky: #c9d9e8;
    --hill: #4f6b4a;
    --hill-dark: #34492f;
  }
  * { margin: 0; padding: 0; box-sizing: border-box; }
  html, body { width: 1200px; height: 900px; overflow: hidden; background: var(--frame-grey); }
  .spread {
    position: absolute; left: 0; top: 24px; width: 1200px; height: 870px;
    background: linear-gradient(100deg, var(--blue-deep) 0%, var(--blue-mid) 45%, var(--blue-light) 100%);
    overflow: hidden;
    font-family: "Carlito", "Calibri", sans-serif;
    color: var(--white);
  }
  .photo {
    position: absolute; top: 0; height: 470px;
    background: linear-gradient(180deg, var(--sky) 0%, #dfe8ef 38%, var(--hill) 58%, var(--hill-dark) 100%);
  }
  .photo--hilltop { left: 0; width: 396px; }
  .photo--climber { left: 402px; width: 396px; background: linear-gradient(180deg, #e4ecf3 0%, #c8d6e2 45%, #56704f 66%, var(--hill-dark) 100%); }
  .photo--tower { left: 804px; width: 396px; background: linear-gradient(180deg, #9dc3ea 0%, #c7dcf0 40%, #5b7a50 60%, #3e5a35 100%); }
  .wave { position: absolute; left: 0; top: 380px; width: 1200px; height: 140px; }
  .column { position: absolute; font-size: 16.5px; line-height: 25px; }
  .column p { margin-bottom: 28px; }
  .col-intro { left: 40px; top: 466px; width: 345px; }
  .col-solutions { left: 436px; top: 466px; width: 356px; }
  .col-more { left: 830px; top: 462px; width: 345px; }
  .section-title {
    font-family: "Cinzel", serif; font-weight: 700; color: var(--orange);
    font-size: 17px; letter-spacing: 1.5px; line-height: 20px; margin-bottom: 30px;
  }
  .col-solutions .section-title { margin-bottom: 14px; }
  .service-title {
    font-family: "Cinzel", serif; font-weight: 700; font-size: 14px; letter-spacing: 1.2px;
    line-height: 18px; margin-top: 4px;
  }
  .col-solutions p { margin-bottom: 18px; }
  .col-more .service-title { margin-top: 0; }
  .col-more p { margin-bottom: 22px; opacity: 0.92; }
  .web-address {
    position: absolute; right: 38px; top: 830px;
    font-family: "Cinzel", serif; font-weight: 700; color: var(--orange);
    font-size: 20px; letter-spacing: 2.5px;
  }
</style>
</head>
<body>
<main class="spread">
  <div class="photo photo--hilltop" role="img" aria-label="Photo of a communications mast and equipment cabinet on a grassy hilltop above a valley"></div>
  <div class="photo photo--climber" role="img" aria-label="Photo of a technician on a mast silhouetted against misty hills"></div>
  <div class="photo photo--tower" role="img" aria-label="Photo of a lattice antenna tower overlooking green rural hills under blue sky"></div>

  <svg class="wave" viewBox="0 0 1200 140" preserveAspectRatio="none" aria-hidden="true">
    <defs>
      <linearGradient id="waveFill" x1="0" y1="0" x2="1" y2="0">
        <stop offset="0" stop-color="#3b72b6"/>
        <stop offset="0.45" stop-color="#5a8ccb"/>
        <stop offset="1" stop-color="#8fb5e0"/>
      </linearGradient>
    </defs>
    <path d="M0 90 C 220 40, 420 40, 620 58 C 820 76, 1000 48, 1200 30 L1200 140 L0 140 Z" fill="url(#waveFill)"/>
    <path d="M0 90 C 220 40, 420 40, 620 58 C 820 76, 1000 48, 1200 30" fill="none" stroke="#a9c8ea" stroke-width="3" opacity="0.7"/>
  </svg>

  <section class="column col-intro">
    <h2 class="section-title">Business-Grade Internet</h2>
    <p>Connecting some of Tasmania’s most rural areas with fast and reliable business-grade internet is what we do best. Brolvix offers options to connect and interconnect your business, no matter where your offices are located. Our team will work with you to determine the best plans, connections and options to suit your business.</p>
    <p>We pride ourselves on being customer-focused and flexible to the changing needs of businesses. We don’t believe you should be stuck with what you have until the end of your plan period, so we will help you adapt your Brolvix package whenever you need us to, easy as that!</p>
  </section>

  <section class="column col-solutions">
    <h2 class="section-title">Brolvix’s Business<br>Internet Solutions</h2>
    <h3 class="service-title">Enterprise Internet</h3>
    <p>For companies requiring the highest quality in speed and reliability for data centre services.</p>
    <h3 class="service-title">Corporate Internet</h3>
    <p>Highly reliable internet that is perfect for everyday company operations such as video conferencing, sending and receiving large files and setting up online storage facilities.</p>
    <h3 class="service-title">Small Business Internet</h3>
    <p>For smaller organisations needing business-grade internet but not quite at the corporate level.</p>
  </section>

  <section class="column col-more">
    <h3 class="service-title">Not sure?</h3>
    <p>Call us – we will explain our services in a language you understand.</p>
    <p>Clever, cost-effective plans. Basic plans starting from $XX.XX...</p>
    <p>We also offer many other computer services for businesses, including Managed Network Services, Server Hosting, Wireless Point-to-Point links, Zephon Wireless LAN and Co-Location and CCTV Services. These solutions are detailed in our Business Services brochure, or on our website.</p>
  </section>

  <a class="web-address">www.brolvix.com.au</a>
</main>
</body>
</html>
```